concept design for a website homepage

Hi, we are looking for a design for Homepage for our childcare centre
We want something really progressive, edgy, modern and premium. We want this website to standout but not cluttered. We only need a Homepage concept design for the below measurements.
1366 Wx768 H
The call to action is join our community
We like the idea of a split screen
Divided into 4 sections screen with the below
Locations and Enrolments
Tandel
Careers
Partnerships
We like angles and shapes, particularly triangles in the designs in the attached examples.
Our company font is Hands of Sean
Have attached some designs that we like the look and feel of and some of our designs from our flyers and some images to use, you don't need to choose all the images, just whatever works with your design.
We have a STEM focus at our centres so something sciency would be great.
Consider in the design will be viewed on desktop and mobile phones
1 page

```html
<!DOCTYPE html>
<html lang="en">
<head>
<meta charset="utf-8">
<title>Tandel – STEM Hub</title>
<link href="https://fonts.googleapis.com/css2?family=Roboto:wght@400;700&family=Tinos&display=swap" rel="stylesheet">
<style>
  :root {
    --backdrop: #9a9a9a;
    --navy: #0b0d45;
    --navy-deep: #05061f;
    --blue: #00a8e8;
    --green: #5db52c;
    --yellow: #d8c300;
    --red: #ee3d24;
    --orange: #ff8533;
    --white: #ffffff;
  }
  html, body {
    margin: 0;
    width: 1200px;
    height: 737px;
    overflow: hidden;
    background: radial-gradient(ellipse at 50% 40%, #a4a4a4 0%, var(--backdrop) 55%, #6e6e6e 100%);
  }
  .stage {
    position: absolute;
    left: 69px;
    top: 70px;
    width: 1062px;
    height: 597px;
    box-shadow: 0 18px 40px rgba(0,0,0,0.45);
    overflow: hidden;
  }
  .homepage {
    position: absolute;
    left: 0;
    top: 0;
    width: 1366px;
    height: 768px;
    transform: scale(0.7775);
    transform-origin: 0 0;
    font-family: "Roboto", Arial, sans-serif;
    color: var(--white);
  }
  .tiles {
    position: absolute;
    inset: 0;
  }
  .hero {
    position: absolute;
    left: 0; top: 0;
    width: 606px; height: 768px;
    background: linear-gradient(160deg, #141a6b 0%, var(--navy) 45%, var(--navy-deep) 100%);
  }
  .brand {
    position: absolute;
    left: 0; width: 606px;
    top: 215px;
    display: flex;
    justify-content: center;
    align-items: center;
    gap: 22px;
  }
  .brand-dot {
    width: 64px; height: 64px;
    border-radius: 50%;
    background: var(--blue);
  }
  .brand-name {
    font-weight: 700;
    font-size: 104px;
    letter-spacing: 2px;
    color: var(--white);
  }
  .hub-title {
    position: absolute;
    left: 0; width: 606px;
    top: 440px;
    text-align: center;
    font-family: "Tinos", "Times New Roman", serif;
    font-size: 88px;
    line-height: 1;
    letter-spacing: 1px;
  }
  .cta {
    position: absolute;
    left: 79px; top: 580px;
    width: 438px; height: 86px;
    border-radius: 43px;
    background: var(--orange);
    display: flex; align-items: center; justify-content: center;
    font-weight: 700; font-size: 26px;
    text-decoration: none; color: var(--white);
  }
  .legal {
    position: absolute;
    left: 0; width: 606px;
    top: 723px;
    text-align: center;
    font-size: 15px;
  }
  .tile-label {
    position: absolute;
    font-weight: 700;
    font-size: 37px;
    line-height: 47px;
    text-align: center;
    transform: translateX(-50%);
    white-space: nowrap;
    letter-spacing: -0.3px;
  }
  .tile-icon {
    position: absolute;
    transform: translate(-50%, -50%);
  }
</style>
</head>
<body>
<div class="stage">
  <main class="homepage">
    <svg class="tiles" viewBox="0 0 1366 768" width="1366" height="768">
      <defs>
        <linearGradient id="photo-lab" x1="0" y1="0" x2="1" y2="1">
          <stop offset="0" stop-color="#0a1a6e" stop-opacity="0"/>
          <stop offset="1" stop-color="#1d2a8c" stop-opacity="0.35"/>
        </linearGradient>
      </defs>
      <rect x="606" y="0" width="760" height="383" fill="var(--green)" role="img" aria-label="Children exploring a science display"/>
      <polygon points="606,0 906,0 1004,383 606,383" fill="var(--blue)" role="img" aria-label="Bright learning centre interior"/>
      <rect x="606" y="383" width="760" height="385" fill="var(--red)" role="img" aria-label="Child with a chicken in a nature activity"/>
      <polygon points="606,383 1072,383 973,768 606,768" fill="var(--yellow)" role="img" aria-label="Child in a hard hat using a drill"/>
      <rect x="0" y="0" width="606" height="768" fill="url(#photo-lab)" role="img" aria-label="Dim science classroom"/>
    </svg>

    <section class="hero">
      <div class="brand">
        <span class="brand-dot"></span>
        <span class="brand-name">Tandel</span>
      </div>
      <h1 class="hub-title" style="margin:0;font-weight:400;">STEM HUB</h1>
      <a class="cta" href="#">JOIN OUR COMMUNITY</a>
      <p class="legal" style="margin:0;">© 2022 Tandel. All rights reserved.Privacy &nbsp;|&nbsp; Terms of Use</p>
    </section>

    <!-- Locations -->
    <svg class="tile-icon" style="left:816px;top:130px" width="80" height="106" viewBox="0 0 80 106">
      <path d="M40 2 C18 2 2 18 2 40 C2 66 40 104 40 104 C40 104 78 66 78 40 C78 18 62 2 40 2 Z" fill="var(--white)"/>
      <circle cx="40" cy="38" r="13" fill="var(--blue)"/>
    </svg>
    <div class="tile-label" style="left:816px;top:222px">LOCATIONS<br>AND ENROLMENTS</div>

    <!-- Tandel -->
    <svg class="tile-icon" style="left:1175px;top:130px" width="112" height="112" viewBox="0 0 112 112">
      <circle cx="54" cy="58" r="46" fill="var(--white)"/>
      <ellipse cx="56" cy="56" rx="58" ry="18" transform="rotate(-40 56 56)" fill="none" stroke="var(--green)" stroke-width="8"/>
      <ellipse cx="56" cy="56" rx="58" ry="18" transform="rotate(-40 56 56)" fill="none" stroke="var(--white)" stroke-width="4"/>
      <circle cx="72" cy="70" r="10" fill="var(--green)"/>
    </svg>
    <div class="tile-label" style="left:1173px;top:222px">TANDEL</div>

    <!-- Careers -->
    <svg class="tile-icon" style="left:781px;top:530px" width="130" height="130" viewBox="0 0 130 130">
      <circle cx="30" cy="14" r="11" fill="var(--white)"/>
      <path d="M20 30 h22 v34 l14 10 v32 h-12 v-26 l-14 -10 l-8 36 h-12 l10 -46 z" fill="var(--white)"/>
      <path d="M30 122 v-12 h28 v-22 h28 v-22 h22" fill="none" stroke="var(--white)" stroke-width="8"/>
      <path d="M108 68 v-40 M96 40 l12 -14 l12 14" fill="none" stroke="var(--white)" stroke-width="8"/>
    </svg>
    <div class="tile-label" style="left:784px;top:649px">CAREERS</div>

    <!-- Partnerships -->
    <svg class="tile-icon" style="left:1173px;top:530px" width="124" height="130" viewBox="0 0 124 130">
      <g fill="var(--white)">
        <polygon points="62,2 68,18 85,18 71,28 76,44 62,34 48,44 53,28 39,18 56,18"/>
        <polygon points="18,20 22,31 34,31 24,38 28,49 18,42 8,49 12,38 2,31 14,31"/>
        <polygon points="106,20 110,31 122,31 112,38 116,49 106,42 96,49 100,38 90,31 102,31"/>
        <path d="M10 78 l26 -20 h24 l-14 12 l8 6 l18 -14 h18 l24 20 l-30 34 l-10 -8 l-8 8 l-8 -6 l-8 8 l-8 -6 l-8 6 z"/>
      </g>
    </svg>
    <div class="tile-label" style="left:1173px;top:649px">PARTNERSHIPS</div>
  </main>
</div>
</body>
</html>
```